QV - menu design

Hi,

We require elegant menu design for upscale restaurant. Please find attached the logo and the menu items for your reference.

for inspiration, this is a good website: -
http://www.platewhisper.example/bellfoldnotes/about.php

We are very much open for Menu Size suggestions.

unfortunately the place is going under renovation, we don't have updated images to it. the closest look and feel to our place is http://varnelo.example ..

we are also open for creative options on the shape, the styles, etc. as long as it represents the fine dine feel ...

Thanks ...

Dear All,

We wouldlike to extend our apology for not being able to provide feedbacks on everysingle design. We were extremely busy and we have multiple contests opensimultaneously which makes the process even harder.

However,we would like to thank you all for the efforts you have put into designingour menu. It is very much appreciated …

We wishyou all success in your design ventures and we are quite positive that we willbe working with many of you on many projects in the soon future. 

Thanks & Regards,

TLG Team...

 

 

 

Industry/Entity Type

Restaurant

Requirements
Must have
• Please ensure that there are 'some' images in the menu ... this is very important.
Should not have
• IMPORTANT: -

1. Please DO NOT insert any currency sign to the menu
2. Please keep the prices of the menu at the end of the menu items descriptions NOT beside the menu item names. The font of the price should be similar to the menu item description and please DO NOT bold the numbers. the prices should be subtle.

Thank you ...

```html
<!DOCTYPE html>
<html lang="en">
<head>
<meta charset="utf-8">
<title>QV Menu – Breakfast &amp; Sandwiches</title>
<link rel="stylesheet" href="https://fonts.googleapis.com/css2?family=Questrial&family=Mulish:ital,wght@0,400;0,700;1,400;1,700&display=swap">
<style>
  :root {
    --backdrop: #d9d6d2;
    --page-light: #fbfaf8;
    --page-shade: #efece8;
    --espresso: #2f221a;
    --espresso-deep: #241a14;
    --heading-brown: #6e4f33;
    --tab-cream: #f4efe8;
    --ink: #2b2b2b;
    --ink-soft: #4a4a4a;
    --cream-text: #efe6da;
    --cream-soft: #cdbfae;
  }
  * { box-sizing: border-box; margin: 0; padding: 0; }
  html, body { width: 1200px; height: 1000px; overflow: hidden; }
  body {
    background: var(--backdrop);
    font-family: "Mulish", Arial, sans-serif;
    position: relative;
  }
  .menu-spread {
    position: absolute;
    left: 40px; top: 110px;
    width: 1120px; height: 780px;
    display: flex;
    box-shadow: 0 14px 40px rgba(0,0,0,0.25);
  }
  .menu-page {
    width: 560px; height: 100%;
    position: relative;
    overflow: hidden;
  }

  /* Breakfast page */
  .page-breakfast {
    background: linear-gradient(90deg, var(--page-light) 0%, var(--page-light) 80%, var(--page-shade) 100%);
  }
  .breakfast-photo {
    position: absolute; left: 0; top: 0;
    width: 100%; height: 180px;
    background: linear-gradient(120deg, #c9a680 0%, #e7d6c0 45%, #b98856 75%, #8a5a30 100%);
  }
  .section-tab {
    position: absolute;
    font-family: "Questrial", Arial, sans-serif;
    font-size: 36px;
    line-height: 1;
    padding: 10px 18px 8px;
  }
  .page-breakfast .section-tab {
    left: 36px; top: 150px;
    background: var(--tab-cream);
    color: var(--heading-brown);
  }
  .page-breakfast .divider-line {
    position: absolute; left: 300px; top: 174px;
    width: 220px; height: 1px;
    background: var(--heading-brown);
    opacity: 0.5;
  }
  .breakfast-list {
    position: absolute; left: 50px; top: 214px; right: 36px;
    list-style: none;
  }
  .menu-item { margin-bottom: 11px; }
  .item-name {
    font-weight: 700;
    font-style: italic;
    font-size: 17px;
    line-height: 1.3;
    color: var(--ink);
    margin-bottom: 2px;
  }
  .item-desc {
    font-style: italic;
    font-size: 12px;
    line-height: 1.42;
    color: var(--ink-soft);
  }
  .page-foot {
    position: absolute; left: 0; right: 0; bottom: 0;
    height: 22px;
    background: var(--espresso);
  }

  /* Sandwich page */
  .page-sandwiches { background: var(--espresso); }
  .sandwich-list {
    position: absolute; left: 36px; top: 24px; right: 30px;
    list-style: none;
  }
  .sandwich-list .menu-item { margin-bottom: 7px; }
  .sandwich-list .item-line {
    font-size: 10.5px;
    line-height: 1.35;
    color: var(--cream-soft);
  }
  .sandwich-list .item-line strong {
    font-family: "Questrial", Arial, sans-serif;
    font-weight: 400;
    font-size: 15px;
    color: var(--cream-text);
    margin-right: 4px;
  }
  .page-sandwiches .section-tab {
    right: 0; top: 252px;
    background: var(--espresso-deep);
    color: var(--tab-cream);
    border-top: 1px solid rgba(255,255,255,0.12);
    padding-right: 26px;
  }
  .page-sandwiches .divider-line {
    position: absolute; left: 120px; top: 276px;
    width: 150px; height: 1px;
    background: var(--cream-soft);
    opacity: 0.5;
  }
  .sandwich-photo {
    position: absolute; left: 0; right: 0; top: 306px; bottom: 0;
    background: radial-gradient(ellipse at 55% 45%, #c48a4c 0%, #8a5a2e 35%, #4a2e1a 70%, #2a1a10 100%);
  }
</style>
</head>
<body>
  <main class="menu-spread">
    <section class="menu-page page-breakfast">
      <div class="breakfast-photo" role="img" aria-label="Breakfast table with coffee, orange juice, oranges, an apple, croissants and toast"></div>
      <h2 class="section-tab">The Breakfast</h2>
      <div class="divider-line"></div>
      <ul class="breakfast-list">
        <li class="menu-item">
          <h3 class="item-name">Butter Croissant</h3>
          <p class="item-desc">Served plain with a selection of two jams, a vanilla custard cream, a chocolate Cream and butter curls). 36</p>
        </li>
        <li class="menu-item">
          <h3 class="item-name">Cheese Croissant</h3>
          <p class="item-desc">Crumbly freshly baked with cheese filling. 29</p>
        </li>
        <li class="menu-item">
          <h3 class="item-name">Daily Fresh Eggs</h3>
          <p class="item-desc">A choice of poached, scrambled, pan fried, omelet) all served with toasted Bread, mushrooms, roasted tomatoes and chicken sausages. 59</p>
        </li>
        <li class="menu-item">
          <h3 class="item-name">Healthy Time</h3>
          <p class="item-desc">One choice of hot beverage from our cafe served with fruit salad, natural Yoghurt, whole wheat bread vegetable sandwiches and sugar free biscuits selection. 49</p>
        </li>
        <li class="menu-item">
          <h3 class="item-name">Energy Time</h3>
          <p class="item-desc">One choice of hot beverage from our cafe served with finger chocolate muffins, Poached egg with toasted bread and crispy beef bacon, crepe roll with goat Cheese and honey and finger chocolate cream with salted cookies.</p>
        </li>
        <li class="menu-item">
          <h3 class="item-name">Third Avenue Time</h3>
          <p class="item-desc">One choice of hot beverage from our cafe served with our selection of scones, Smoked salmon and avocado sandwich, roasted sausages sandwich, grilled vegetables sandwich, selection of our best biscuits. 59</p>
        </li>
        <li class="menu-item">
          <h3 class="item-name">The Arabic Breakfast</h3>
          <p class="item-desc">Choice of Zattar Manakish and Cheese Manakish, served with one choice of hot beverage from our cafe and fresh orange juice. 59</p>
        </li>
      </ul>
      <div class="page-foot"></div>
    </section>

    <section class="menu-page page-sandwiches">
      <ul class="sandwich-list">
        <li class="menu-item"><p class="item-line"><strong>Grilled Vegetables Sandwich</strong> with fresh Goat cheese and chives served with our Homemade spicy garlic mayo. 59</p></li>
        <li class="menu-item"><p class="item-line"><strong>Butterfish burger</strong> with fresh tomato, beef bacon, grilled vegetables and bearnaise sauce. Tataki Tuna sandwich with red onion slices, stewed endives and black olives and sultanas pate'. 79</p></li>
        <li class="menu-item"><p class="item-line"><strong>Beef sirloin steak sandwich</strong> with grain mustard, Parmesan cheese and fresh Nashi pears. 79</p></li>
        <li class="menu-item"><p class="item-line"><strong>The Traditional Club sandwich</strong> served with French fries and vegetable chips. 69</p></li>
        <li class="menu-item"><p class="item-line"><strong>Chicken sandwich</strong> with Parmesan cheese slices, sundried tomatoes and mint Flavored mayo. 59</p></li>
      </ul>
      <div class="divider-line"></div>
      <h2 class="section-tab">The Sandwiches</h2>
      <div class="sandwich-photo" role="img" aria-label="Toasted bacon and lettuce sandwich on a brown linen napkin"></div>
    </section>
  </main>
</body>
</html>
```